Trailer wrap for home remodeling company in Sarasota County Florida

I need a wrap design for an enclosed trailer. I like the idea of adding a picture of a really nice kitchen or bathroom, possibly a before and after.
Matte black background
Must include the below information
Brindle Oak Remodeling
CGC2807391
941-527–8140
www.brindleoakremodeling.example
Bathrooms,Kitchens, Additions, Remodels
Trusted Expertise. Refined Design
Trailer is currently all black
Updates

Designs are not what we are looking for, very busy

Industry/Entity Type

Home Remodeling

Colors
0054AA
0677BA
7BADD7
CADEEF
E8F1F8

Requirements
Must have
• Matte black background

```html
<!DOCTYPE html>
<html lang="en">
<head>
<meta charset="utf-8">
<title>Brindle Oak Remodeling – Trailer Wrap</title>
<link href="https://fonts.googleapis.com/css2?family=Cinzel:wght@400&family=Poppins:wght@600;700;800&display=swap" rel="stylesheet">
<style>
  :root{
    --matte-top:#26272b;
    --matte-bottom:#141517;
    --matte-deep:#111214;
    --accent:#4f8ff0;
    --accent-bright:#2f6fe0;
    --white:#ffffff;
    --band:#3a3a3c;
    --ink:#1b1b1f;
    --stage:#f3f4f6;
    --photo-kitchen-a:#d9dcdf;
    --photo-kitchen-b:#8f9398;
    --photo-bath-a:#8a6a4f;
    --photo-bath-b:#3b2c22;
    --photo-tub-a:#6f6c69;
    --photo-tub-b:#2e2d2c;
  }
  html,body{margin:0;padding:0;}
  body{
    width:744px;height:1200px;overflow:hidden;
    background:var(--stage);
    position:relative;
  }
  .wrap-panel{position:absolute;display:block;}
  .side-left{left:20px;top:20px;width:704px;height:290px;}
  .side-right{left:20px;top:330px;width:704px;height:290px;}
  .rear-doors{left:20px;top:660px;width:345px;height:400px;}
  .ramp-door{left:385px;top:660px;width:339px;height:420px;}

  .brand-name{font-family:"Cinzel",serif;font-weight:400;fill:var(--white);}
  .brand-sub{font-family:"Cinzel",serif;font-weight:400;fill:var(--white);}
  .web-band-text{font-family:"Poppins",sans-serif;font-weight:800;fill:var(--white);}
  .services{font-family:"Poppins",sans-serif;font-weight:700;fill:var(--ink);}
  .phone{font-family:"Poppins",sans-serif;font-weight:800;fill:var(--white);}
  .phone-dark{fill:var(--ink);}
  .phone-blue{font-family:"Poppins",sans-serif;font-weight:800;fill:var(--accent);}
  .tagline{font-family:"Poppins",sans-serif;font-weight:700;fill:var(--white);}
  .tagline-blue{font-family:"Poppins",sans-serif;font-weight:700;fill:var(--accent);}
  .license{font-family:"Poppins",sans-serif;font-weight:800;fill:var(--white);}
  .license-blue{font-family:"Poppins",sans-serif;font-weight:800;fill:var(--accent);}
  .small-ink{font-family:"Poppins",sans-serif;font-weight:700;fill:var(--ink);}
  .rule{stroke:var(--white);stroke-width:1.2;}
</style>
</head>
<body>

<svg class="wrap-panel side-left" viewBox="0 0 704 290" aria-label="Trailer left side wrap">
  <defs>
    <linearGradient id="matteFill" x1="0" y1="0" x2="1" y2="1">
      <stop offset="0" stop-color="var(--matte-top)"/>
      <stop offset="1" stop-color="var(--matte-bottom)"/>
    </linearGradient>
    <linearGradient id="kitchenFill" x1="0" y1="0" x2="0" y2="1">
      <stop offset="0" stop-color="var(--photo-kitchen-a)"/>
      <stop offset="1" stop-color="var(--photo-kitchen-b)"/>
    </linearGradient>
    <linearGradient id="bathFill" x1="0" y1="0" x2="1" y2="1">
      <stop offset="0" stop-color="var(--photo-bath-a)"/>
      <stop offset="1" stop-color="var(--photo-bath-b)"/>
    </linearGradient>
    <linearGradient id="tubFill" x1="0" y1="0" x2="0" y2="1">
      <stop offset="0" stop-color="var(--photo-tub-a)"/>
      <stop offset="1" stop-color="var(--photo-tub-b)"/>
    </linearGradient>
  </defs>
  <rect class="panel-bg" width="704" height="290" fill="url(#matteFill)"/>

  <polygon class="accent-stripe" points="430,0 445,0 360,200 345,200" fill="var(--accent-bright)"/>
  <polygon class="photo-frame" points="455,0 640,0 600,100 415,100" fill="var(--white)"/>
  <polygon class="photo tub-photo" role="img" aria-label="Photo: modern bathroom with freestanding tub" points="463,0 630,0 594,92 427,92" fill="url(#tubFill)"/>
  <polygon class="accent-stripe" points="648,0 662,0 585,205 571,205" fill="var(--accent-bright)"/>

  <polygon class="white-band" points="35,290 100,108 590,108 568,166 232,166 190,290" fill="var(--white)"/>
  <polygon class="accent-stripe" points="25,290 90,108 98,108 33,290" fill="var(--accent-bright)"/>
  <polygon class="photo kitchen-photo" role="img" aria-label="Photo: bright modern kitchen with island" points="110,116 238,116 218,168 90,168" fill="url(#kitchenFill)"/>
  <polygon class="photo bath-photo" role="img" aria-label="Photo: warm wood bathroom vanity" points="78,198 208,198 176,290 46,290" fill="url(#bathFill)"/>

  <polygon class="web-band" points="248,115 585,115 576,139 239,139" fill="var(--band)"/>
  <text class="web-band-text" x="412" y="132" font-size="10.5" letter-spacing="3.2" text-anchor="middle">BRINDLEOAKREMODELING.EXAMPLE</text>
  <text class="services" x="246" y="158" font-size="11">BATHROOMS,KITCHENS, ADDITIONS, REMODELS</text>

  <polygon class="phone-band" points="232,170 448,170 434,206 218,206" fill="var(--accent)"/>
  <text class="phone" x="240" y="197" font-size="22.5">941-527–<tspan class="phone-dark">8140</tspan></text>

  <text class="tagline" x="458" y="185" font-size="12">TRUSTED EXPERTISE</text>
  <text class="tagline" x="458" y="202" font-size="12">REFINED DESIGN</text>

  <polygon class="license-band" points="452,220 704,220 704,250 442,250" fill="var(--accent)"/>
  <text class="license" x="456" y="243" font-size="18">CGC2807391</text>

  <text class="brand-name" x="275" y="64" font-size="30" letter-spacing="3" text-anchor="middle">BRINDLE OAK</text>
  <line class="rule" x1="145" y1="84" x2="203" y2="84"/>
  <text class="brand-sub" x="275" y="88" font-size="12" letter-spacing="5" text-anchor="middle">REMODELING</text>
  <line class="rule" x1="347" y1="84" x2="405" y2="84"/>
</svg>

<svg class="wrap-panel side-right" viewBox="0 0 704 290" aria-label="Trailer right side wrap">
  <rect class="panel-bg" width="704" height="290" fill="url(#matteFill)"/>

  <polygon class="photo-frame" points="22,0 196,0 236,95 62,95" fill="var(--white)"/>
  <polygon class="photo tub-photo" role="img" aria-label="Photo: modern bathroom with freestanding tub" points="32,0 188,0 224,88 68,88" fill="url(#tubFill)"/>
  <polygon class="accent-stripe" points="204,0 216,0 258,100 246,100" fill="var(--accent-bright)"/>
  <polygon class="accent-stripe" points="0,0 12,0 80,170 68,170" fill="var(--accent-bright)"/>

  <polygon class="white-band" points="95,108 545,108 640,290 480,290 432,166 118,166" fill="var(--white)"/>
  <polygon class="accent-stripe" points="547,108 557,108 652,290 642,290" fill="var(--accent-bright)"/>
  <polygon class="photo kitchen-photo" role="img" aria-label="Photo: bright modern kitchen with island" points="440,115 537,115 563,170 466,170" fill="url(#kitchenFill)"/>
  <polygon class="photo bath-photo" role="img" aria-label="Photo: warm wood bathroom vanity" points="470,180 572,180 618,288 508,288" fill="url(#bathFill)"/>

  <polygon class="web-band" points="105,115 425,115 415,139 112,139" fill="var(--band)"/>
  <text class="web-band-text" x="263" y="132" font-size="10" letter-spacing="3" text-anchor="middle">BRINDLEOAKREMODELING.EXAMPLE</text>
  <text class="services" x="120" y="158" font-size="11">BATHROOMS,KITCHENS, ADDITIONS, REMODELS</text>

  <polygon class="phone-band" points="225,170 445,170 432,204 212,204" fill="var(--accent)"/>
  <text class="phone" x="232" y="196" font-size="22">941-527–<tspan class="phone-dark">8140</tspan></text>

  <text class="tagline" x="200" y="184" font-size="11.5" text-anchor="end">TRUSTED EXPERTISE</text>
  <text class="tagline" x="200" y="200" font-size="11.5" text-anchor="end">REFINED DESIGN</text>

  <polygon class="license-band" points="0,212 206,212 212,242 0,242" fill="var(--accent)"/>
  <text class="license" x="48" y="234" font-size="17">CGC2807391</text>

  <text class="brand-name" x="450" y="62" font-size="30" letter-spacing="3" text-anchor="middle">BRINDLE OAK</text>
  <line class="rule" x1="320" y1="82" x2="378" y2="82"/>
  <text class="brand-sub" x="450" y="86" font-size="12" letter-spacing="5" text-anchor="middle">REMODELING</text>
  <line class="rule" x1="522" y1="82" x2="580" y2="82"/>
</svg>

<svg class="wrap-panel rear-doors" viewBox="0 0 345 400" aria-label="Trailer rear barn doors wrap">
  <g class="door door-left">
    <rect width="170" height="400" fill="url(#matteFill)"/>
    <text class="brand-name" x="85" y="92" font-size="15" letter-spacing="1.5" text-anchor="middle">BRINDLE OAK</text>
    <line class="rule" x1="18" y1="107" x2="44" y2="107"/>
    <text class="brand-sub" x="85" y="110" font-size="7" letter-spacing="2.5" text-anchor="middle">REMODELING</text>
    <line class="rule" x1="126" y1="107" x2="152" y2="107"/>
    <polygon points="0,245 28,205 170,205 170,400 0,400" fill="var(--accent-bright)"/>
    <polygon points="6,400 6,248 32,212 170,212 170,400" fill="var(--white)"/>
    <rect x="30" y="222" width="140" height="18" fill="var(--band)"/>
    <text class="web-band-text" x="160" y="230" font-size="5.5" text-anchor="end">TRUSTED EXPERTISE</text>
    <text class="web-band-text" x="160" y="237" font-size="5.5" text-anchor="end">REFINED DESIGN</text>
    <rect x="6" y="252" width="94" height="18" fill="var(--accent)"/>
    <text class="license" x="12" y="265" font-size="9">CGC2807391</text>
    <text class="small-ink" x="158" y="254" font-size="5.5" text-anchor="end">BATHROOMS •</text>
    <text class="small-ink" x="158" y="263" font-size="5.5" text-anchor="end">KITCHENS •</text>
    <text class="small-ink" x="158" y="272" font-size="5.5" text-anchor="end">ADDITIONS •</text>
    <text class="small-ink" x="158" y="281" font-size="5.5" text-anchor="end">REMODELS •</text>
    <text class="phone-blue" x="88" y="306" font-size="14" text-anchor="middle">941-527–<tspan class="phone-dark">8140</tspan></text>
    <text class="small-ink" x="88" y="320" font-size="5.6" text-anchor="middle">BRINDLEOAKREMODELING.EXAMPLE</text>
  </g>
  <g class="door door-right" transform="translate(175 0)">
    <rect width="170" height="400" fill="url(#matteFill)"/>
    <text class="brand-name" x="85" y="92" font-size="15" letter-spacing="1.5" text-anchor="middle">BRINDLE OAK</text>
    <line class="rule" x1="18" y1="107" x2="44" y2="107"/>
    <text class="brand-sub" x="85" y="110" font-size="7" letter-spacing="2.5" text-anchor="middle">REMODELING</text>
    <line class="rule" x1="126" y1="107" x2="152" y2="107"/>
    <polygon points="0,205 142,205 170,245 170,400 0,400" fill="var(--accent-bright)"/>
    <polygon points="0,212 138,212 164,248 164,400 0,400" fill="var(--white)"/>
    <rect x="0" y="222" width="140" height="18" fill="var(--band)"/>
    <text class="web-band-text" x="10" y="230" font-size="5.5">TRUSTED EXPERTISE</text>
    <text class="web-band-text" x="10" y="237" font-size="5.5">REFINED DESIGN</text>
    <rect x="70" y="252" width="94" height="18" fill="var(--accent)"/>
    <text class="license" x="76" y="265" font-size="9">CGC2807391</text>
    <text class="small-ink" x="12" y="254" font-size="5.5">• BATHROOMS</text>
    <text class="small-ink" x="12" y="263" font-size="5.5">• KITCHENS</text>
    <text class="small-ink" x="12" y="272" font-size="5.5">• ADDITIONS</text>
    <text class="small-ink" x="12" y="281" font-size="5.5">• REMODELS</text>
    <text class="phone-blue" x="82" y="306" font-size="14" text-anchor="middle">941-527–<tspan class="phone-dark">8140</tspan></text>
    <text class="small-ink" x="82" y="320" font-size="5.6" text-anchor="middle">BRINDLEOAKREMODELING.EXAMPLE</text>
  </g>
</svg>

<svg class="wrap-panel ramp-door" viewBox="0 0 339 420" aria-label="Trailer rear ramp door wrap">
  <rect width="339" height="420" fill="url(#matteFill)"/>
  <text class="brand-name" x="170" y="118" font-size="29" letter-spacing="2.5" text-anchor="middle">BRINDLE OAK</text>
  <line class="rule" x1="40" y1="148" x2="102" y2="148"/>
  <text class="brand-sub" x="170" y="152" font-size="12" letter-spacing="4" text-anchor="middle">REMODELING</text>
  <line class="rule" x1="238" y1="148" x2="300" y2="148"/>
  <text class="phone" x="170" y="197" font-size="27" text-anchor="middle">941-527–8140</text>

  <polygon points="0,210 30,246 270,246 305,210 339,210 339,420 0,420" fill="var(--accent-bright)"/>
  <polygon points="0,222 26,254 276,254 310,222 339,222 339,420 0,420" fill="var(--white)"/>

  <rect x="0" y="264" width="175" height="28" fill="var(--band)"/>
  <text class="license-blue" x="20" y="284" font-size="16">CGC2807391</text>
  <text class="tagline-blue" x="172" y="311" font-size="11" text-anchor="end">TRUSTED EXPERTISE</text>
  <text class="tagline-blue" x="172" y="325" font-size="11" text-anchor="end">REFINED DESIGN</text>
  <text class="small-ink" x="322" y="278" font-size="10" text-anchor="end">BATHROOMS •</text>
  <text class="small-ink" x="322" y="292" font-size="10" text-anchor="end">KITCHENS •</text>
  <text class="small-ink" x="322" y="306" font-size="10" text-anchor="end">ADDITIONS •</text>
  <text class="small-ink" x="322" y="320" font-size="10" text-anchor="end">REMODELS •</text>

  <polygon points="30,368 300,368 322,398 8,398" fill="var(--accent-bright)"/>
  <polygon points="38,374 292,374 312,402 18,402" fill="var(--matte-deep)"/>
  <text class="web-band-text" x="165" y="393" font-size="10.5" text-anchor="middle">BRINDLEOAKREMODELING.EXAMPLE</text>
  <rect x="0" y="402" width="339" height="18" fill="var(--accent-bright)"/>
</svg>

</body>
</html>
```